Business card design needed

Hello, I Need a business card for a company that specialises in providing contract management services for civil construction projects - roads, bridges etc.
I do have a logo that i produced for PLOVER Civilworks however it probably needs a little work, the circles dont have defined edges, i was thinking the colours should reflect the dry interior of Australia progressing out to the colours of the ocean as you move towards the East.... that was my thinking anyway!
Target Market(s)
Professional people generally 30+ yrs old who need professional services to deliver contracts in a high risk environment
Industry/Entity Type
Construction
Contact Information for Business Card
PLOVER Civilworks
Darren Holbeck - Director and Principal Engineer
Registered Professional Engineer of Queensland
Phone 0438 615 272
Email darren@plovercivilworks.com.au
ABN 83 214 570 618
Logo Text
PLOVER Civilworks
Logo styles of interest
Pictorial/Combination Logo
Wordmark Logo
Lettermark Logo
Look and feel

```html
<!DOCTYPE html>
<html lang="en">
<head>
<meta charset="UTF-8">
<title>PLOVER Civilworks – Business Card</title>
<link rel="stylesheet" href="https://fonts.googleapis.com/css2?family=Open+Sans:wght@300;400;600;700&display=swap">
<style>
  :root {
    --backdrop-light: #b9bfc2;
    --backdrop-dark: #7d8789;
    --card-white: #ffffff;
    --charcoal: #1f2126;
    --charcoal-soft: #2b2f36;
    --band-grey: #8c9697;
    --band-grey-light: #a3acad;
    --ink: #222428;
    --accent-orange: #e8561a;
    --text-light: #e6e8ea;
    --icon-grey: #a9aeb3;
    --stitch: #9aa0a5;
    --mark-red: #b5232a;
  }
  * { box-sizing: border-box; margin: 0; padding: 0; }
  html, body { width: 1200px; height: 1000px; overflow: hidden; }
  body {
    font-family: "Open Sans", Arial, sans-serif;
    background: radial-gradient(ellipse at 20% 10%, var(--backdrop-light), var(--backdrop-dark));
    position: relative;
  }
  .card {
    position: absolute;
    left: 250px;
    width: 700px;
    height: 400px;
    overflow: hidden;
    box-shadow: 0 10px 24px rgba(0,0,0,0.3);
  }
  .card--front { top: 60px; background: var(--card-white); }
  .card--back {
    top: 540px;
    background: linear-gradient(100deg, var(--charcoal) 0%, var(--charcoal-soft) 45%, var(--charcoal) 100%);
  }

  /* Front */
  .front__top {
    height: 215px;
    display: flex;
    align-items: center;
    padding-left: 48px;
  }
  .front__divider {
    height: 12px;
    background: var(--card-white);
    border-top: 2px solid var(--stitch);
    border-bottom: 2px dashed var(--stitch);
  }
  .front__bottom {
    position: absolute;
    left: 0; right: 0; bottom: 0;
    top: 229px;
    background: linear-gradient(100deg, var(--charcoal) 0%, var(--charcoal-soft) 50%, var(--charcoal) 100%);
    color: var(--text-light);
  }
  .brand {
    display: flex;
    align-items: center;
    gap: 18px;
  }
  .brand__dot {
    width: 46px; height: 46px;
    border-radius: 50%;
    background: var(--mark-red);
  }
  .brand__name {
    font-size: 40px;
    font-weight: 400;
    color: var(--ink);
    letter-spacing: 0.5px;
  }
  .person {
    position: absolute;
    left: 48px;
    bottom: 48px;
  }
  .person__name {
    font-size: 28px;
    font-weight: 600;
    color: var(--accent-orange);
    line-height: 1.1;
  }
  .person__title {
    font-size: 12px;
    margin-top: 6px;
    padding-left: 14px;
  }
  .contact {
    position: absolute;
    left: 420px;
    top: 26px;
    list-style: none;
    font-size: 14px;
    font-weight: 300;
  }
  .contact__item {
    display: flex;
    align-items: center;
    gap: 12px;
    margin-bottom: 10px;
  }
  .contact__icon { width: 18px; height: 18px; fill: var(--icon-grey); }
  .abn {
    position: absolute;
    right: 30px;
    bottom: 22px;
    font-size: 14px;
    font-weight: 300;
  }
  .abn__label { color: var(--accent-orange); font-weight: 600; margin-right: 4px; }

  /* Back */
  .back__band {
    position: absolute;
    left: 0; right: 0;
    top: 110px;
    height: 180px;
    background: linear-gradient(100deg, var(--band-grey) 0%, var(--band-grey-light) 50%, var(--band-grey) 100%);
    display: flex;
    align-items: center;
    justify-content: center;
  }
  .back__band .brand__dot { width: 60px; height: 60px; }
  .back__band .brand__name { font-size: 48px; }
</style>
</head>
<body>
  <section class="card card--front" aria-label="Business card front">
    <div class="front__top">
      <div class="brand">
        <span class="brand__dot"></span>
        <span class="brand__name">PLOVER Civilworks</span>
      </div>
    </div>
    <div class="front__divider"></div>
    <div class="front__bottom">
      <div class="person">
        <p class="person__name">Darren Holbeck</p>
        <p class="person__title">Director and Principal Engineer</p>
      </div>
      <ul class="contact">
        <li class="contact__item">
          <svg class="contact__icon" viewBox="0 0 24 24" aria-hidden="true"><path d="M6.6 10.8a15.1 15.1 0 0 0 6.6 6.6l2.2-2.2a1 1 0 0 1 1-.25 11.4 11.4 0 0 0 3.6.57 1 1 0 0 1 1 1V20a1 1 0 0 1-1 1A17 17 0 0 1 3 4a1 1 0 0 1 1-1h3.5a1 1 0 0 1 1 1c0 1.25.2 2.45.57 3.57a1 1 0 0 1-.25 1z"/></svg>
          <span>0438 615 272</span>
        </li>
        <li class="contact__item">
          <svg class="contact__icon" viewBox="0 0 24 24" aria-hidden="true"><path d="M2 5h20v14H2z M2 5l10 8 10-8" fill="none" stroke="#a9aeb3" stroke-width="2"/></svg>
          <span>darren@plovercivilworks.com.au</span>
        </li>
      </ul>
      <p class="abn"><span class="abn__label">ABN</span>83 214 570 618</p>
    </div>
  </section>

  <section class="card card--back" aria-label="Business card back">
    <div class="back__band">
      <div class="brand">
        <span class="brand__dot"></span>
        <span class="brand__name">PLOVER Civilworks</span>
      </div>
    </div>
  </section>
</body>
</html>
```